Harbor Bloom Nutraceutical Website

Need a website for a vitamin gummy manufacturing and white-labeling company based in Charleston, SC. We service Zelvorn brands, Ecommerce brands, and any customer needing supplement gummies white labeled. I added out logos for color and style. We have always used navy blue, gold, and white in our color palet, we decided to add purple into the logo.

Our partner's website, that makes caples and powders, is https://www.brelmoxworks.com/

We are just now moving into our facility and don't have pictures or videos of the space, equipement, products, etc. I attached the flyer for the machine we have as reference.

The site just needs to be a simple landing page for now. 'Request Quote' for sales leads and 'enquire here' for job applications. I just need a simple site so we can have our state's dept of commerce announce us publicly.

There are 2 logos. We will be using 'Harbor Bloom Nutraceutical' for now. I cannot use "HB Nutra" until I have approval from our state, but "HB nutra" will be the end logo for use after a couple of months.

```html
<!DOCTYPE html>
<html lang="en">
<head>
<meta charset="utf-8">
<title>Harbor Bloom Nutraceutical</title>
<link href="https://fonts.googleapis.com/css2?family=Lexend:wght@400;500;600&family=Montserrat:wght@400;500;600&display=swap" rel="stylesheet">
<style>
:root{
  --navy:#2b3e6b;
  --navy-dark:#1f2f57;
  --sky:#8ec5e6;
  --purple:#7a1b86;
  --ink:#1d1d1d;
  --grey:#efefef;
  --line:#c9cfdc;
  --white:#ffffff;
}
*{margin:0;padding:0;box-sizing:border-box}
html,body{width:1200px;height:3938px;overflow:hidden}
body{position:relative;background:var(--white);font-family:"Montserrat",sans-serif;color:var(--ink)}
.abs{position:absolute}
.display{font-family:"Lexend",sans-serif;font-weight:500;letter-spacing:1px;text-transform:uppercase}

/* header */
.site-header{position:absolute;left:0;top:0;width:1200px;height:115px;background:var(--white);z-index:3}
.logo-tab{position:absolute;left:176px;top:80px;width:290px;height:66px;background:var(--white);border-radius:0 0 40px 40px;z-index:4}
.logo{position:absolute;left:127px;top:48px;width:393px;text-align:center;z-index:5;color:var(--navy)}
.logo .name{font-family:"Lexend",sans-serif;font-weight:500;font-size:36px;letter-spacing:2px;line-height:42px;display:block}
.logo .sub{font-family:"Lexend",sans-serif;font-weight:500;font-size:27px;letter-spacing:2px;line-height:32px;display:block}
.topbar{position:absolute;top:20px;left:608px;font-size:13px;color:#333;display:flex;align-items:center;gap:14px}
.enquire{position:absolute;left:930px;top:12px;width:137px;height:34px;border-radius:17px;background:var(--navy);color:#fff;font-size:13px;font-weight:500;display:flex;align-items:center;justify-content:center}
.header-rule{position:absolute;left:573px;top:60px;width:494px;height:1px;background:#999}
.nav a{position:absolute;top:82px;font-size:12px;font-weight:600;color:#111;text-decoration:none}
.nav a.active{color:var(--navy)}

/* hero */
.hero{position:absolute;left:0;top:115px;width:1200px;height:504px;background:linear-gradient(100deg,#1b2435 0%,#222b3c 55%,#2a3142 100%)}
.hero-photo{position:absolute;left:580px;top:40px;width:505px;height:460px;border-radius:20px;background:radial-gradient(ellipse at 60% 50%,#d9862a 0%,#b3401e 40%,#5a5a3a 70%,rgba(40,48,64,0) 100%)}
.hero-band{position:absolute;left:0;top:619px;width:1200px;height:8px;background:var(--purple)}
.hero-welcome{left:133px;top:238px;color:#fff;font-size:22px}
.hero-title{left:133px;top:290px;color:#fff;font-size:46px;line-height:77px}
.btn-start{left:133px;top:460px;width:193px;height:57px;border-radius:29px;background:var(--navy);color:#fff;font-size:20px;font-weight:500;display:flex;align-items:center;justify-content:center}

/* products */
.section-title{position:absolute;left:0;width:1200px;text-align:center;color:var(--navy);font-size:34px}
.feature-card{position:absolute;left:446px;top:800px;width:314px;height:431px;border:1px solid #ddd;border-radius:16px;box-shadow:0 2px 8px rgba(0,0,0,.12);background:#fff}
.product-photo{position:absolute;width:280px;height:190px;border-radius:16px}
.product-name{position:absolute;width:340px;text-align:center;color:var(--navy);font-size:20px}
.product-text{position:absolute;width:340px;text-align:center;font-size:14px;line-height:34px}
.btn-more{position:absolute;width:171px;height:38px;border-radius:19px;background:#fff;box-shadow:0 1px 5px rgba(0,0,0,.2);color:var(--navy);font-size:13px;font-weight:600;display:flex;align-items:center;justify-content:center;gap:12px}
.btn-more.solid{background:var(--navy);color:#fff;box-shadow:none}
.btn-outline{position:absolute;border:2px solid var(--navy);border-radius:30px;color:var(--navy);font-weight:500;display:flex;align-items:center;justify-content:center}

/* quote */
.quote{position:absolute;left:0;top:1842px;width:1200px;height:508px;background:var(--navy)}
.candy{position:absolute;border-radius:40px}
.field{position:absolute;border-bottom:1px solid #d9deea;color:#fff;font-size:13px;font-weight:600;display:flex;justify-content:space-between;align-items:flex-end;padding-bottom:10px}
.field svg{fill:currentColor}
.btn-send{position:absolute;left:504px;top:2224px;width:193px;height:57px;border:2px solid #fff;border-radius:29px;color:#fff;font-size:20px;font-weight:500;display:flex;align-items:center;justify-content:center}

/* about */
.about-frame{position:absolute;left:125px;top:2438px;width:467px;height:416px;border-left:2px solid #111;border-top:2px solid #111}
.about-photo{position:absolute;left:133px;top:2446px;width:466px;height:408px;background:linear-gradient(135deg,#e44a1c 0%,#f6a21c 40%,#d92428 70%,#f1c23c 100%)}
.about-title{left:651px;top:2478px;color:var(--navy);font-size:34px}
.about-text{left:651px;top:2543px;width:395px;font-size:14px;line-height:34px}

/* careers */
.careers{position:absolute;left:0;top:2943px;width:1200px;height:662px;background:var(--grey)}
.career-card{position:absolute;left:133px;top:3030px;width:934px;height:486px;background:#fff}
.career-photo{position:absolute;left:619px;top:3044px;width:436px;height:457px;background:linear-gradient(160deg,#8a8a5a 0%,#e2762a 35%,#c43a58 65%,#8fb23a 100%)}
.career-title{left:168px;top:3068px;color:var(--navy);font-size:32px;line-height:52px}
.field.dark{color:#111;border-bottom-color:#333}

/* footer */
.site-footer{position:absolute;left:0;top:3605px;width:1200px;height:333px;background:var(--navy);color:#fff}
.footer-links a{position:absolute;left:138px;color:#fff;font-size:14px;text-decoration:none;font-weight:500}
.footer-divider{position:absolute;top:52px;width:1px;height:168px;background:rgba(255,255,255,.3)}
.footer-logo{position:absolute;left:340px;top:95px;width:470px;text-align:center}
.footer-logo .name{font-family:"Lexend",sans-serif;font-weight:500;font-size:38px;letter-spacing:2px;display:block;line-height:44px}
.footer-logo .sub{font-family:"Lexend",sans-serif;font-weight:500;font-size:28px;letter-spacing:3px;display:block;line-height:34px}
.footer-contact{position:absolute;left:906px;font-size:14px;line-height:30px;font-weight:500}
.footer-rule{position:absolute;left:133px;top:271px;width:934px;height:1px;background:rgba(255,255,255,.35)}
.copyright{position:absolute;left:0;top:296px;width:1200px;text-align:center;font-size:11px;font-weight:500}
</style>
</head>
<body>

<header class="site-header">
  <div class="topbar">
    <span>CALL US TODAY</span>
    <svg width="14" height="14" viewBox="0 0 24 24" fill="#2b3e6b"><path d="M6.6 10.8a15 15 0 0 0 6.6 6.6l2.2-2.2c.3-.3.7-.4 1-.2 1.1.4 2.3.6 3.6.6.6 0 1 .4 1 1V20c0 .6-.4 1-1 1A17 17 0 0 1 3 4c0-.6.4-1 1-1h3.5c.6 0 1 .4 1 1 0 1.3.2 2.5.6 3.6.1.3 0 .7-.2 1z"/></svg>
    <span>+1 555 014 2290</span>
  </div>
  <div class="enquire">ENQUIRE HERE</div>
  <div class="header-rule"></div>
  <nav class="nav">
    <a class="active" style="left:656px">HOME</a>
    <a style="left:735px">ABOUT US</a>
    <a style="left:841px">OUR PRODUCTS</a>
    <a style="left:986px">CONTACT US</a>
  </nav>
</header>
<div class="logo-tab"></div>
<div class="logo"><span class="name">HARBOR BLOOM</span><span class="sub">NUTRACEUTICAL</span></div>

<section class="hero">
  <div class="hero-photo" role="img" aria-label="Glass jars filled with colourful gummy bears on a wooden table"></div>
</section>
<div class="abs display hero-welcome">Welcome to</div>
<h1 class="abs display hero-title">Harbor Bloom<br>Nutraceutical</h1>
<div class="abs btn-start">GET STARTED</div>
<div class="hero-band"></div>

<h2 class="section-title display" style="top:704px">Our Products</h2>
<div class="feature-card"></div>

<div class="product-photo" style="left:119px;top:819px;background:linear-gradient(135deg,#3a2a1e,#c2461a 55%,#e9b21c)" role="img" aria-label="Gummy production line in a factory"></div>
<div class="product-photo" style="left:463px;top:819px;background:linear-gradient(135deg,#2a1f22,#8c1a2a 50%,#d8c8c8)" role="img" aria-label="Red gummies on a curved conveyor"></div>
<div class="product-photo" style="left:800px;top:819px;background:linear-gradient(135deg,#5a6a8a,#c9ced8 45%,#e2762a)" role="img" aria-label="Gummy packing machine"></div>
<div class="product-photo" style="left:119px;top:1275px;background:linear-gradient(135deg,#e64a8a,#f2c23a 50%,#4ab2d8)" role="img" aria-label="Colourful gummies pouring from a machine"></div>
<div class="product-photo" style="left:459px;top:1275px;background:linear-gradient(135deg,#1c2a4a,#d8337a 55%,#3a5a9a)" role="img" aria-label="Pink gummies on a production belt"></div>
<div class="product-photo" style="left:800px;top:1275px;background:linear-gradient(135deg,#f28a6a,#f4a64a 50%,#f0c860)" role="img" aria-label="Sugared gummies in trays"></div>

<h3 class="product-name display" style="left:89px;top:1036px">Lorem Ipsum</h3>
<h3 class="product-name display" style="left:434px;top:1036px">Lorem Ipsum</h3>
<h3 class="product-name display" style="left:773px;top:1036px">Lorem Ipsum</h3>
<h3 class="product-name display" style="left:89px;top:1492px">Lorem Ipsum</h3>
<h3 class="product-name display" style="left:433px;top:1492px">Lorem Ipsum</h3>
<h3 class="product-name display" style="left:773px;top:1492px">Lorem Ipsum</h3>

<p class="product-text" style="left:89px;top:1071px">Sed ut perspiciatis unde omnis iste<br>natus error sit voluptatem</p>
<p class="product-text" style="left:434px;top:1071px">Sed ut perspiciatis unde omnis iste<br>natus error sit voluptatem</p>
<p class="product-text" style="left:773px;top:1071px">Sed ut perspiciatis unde omnis iste<br>natus error sit voluptatem</p>
<p class="product-text" style="left:89px;top:1527px">Sed ut perspiciatis unde omnis iste<br>natus error sit voluptatem</p>
<p class="product-text" style="left:433px;top:1527px">Sed ut perspiciatis unde omnis iste<br>natus error sit voluptatem</p>
<p class="product-text" style="left:773px;top:1527px">Sed ut perspiciatis unde omnis iste<br>natus error sit voluptatem</p>

<div class="btn-more" style="left:173px;top:1155px"><svg width="24" height="10" viewBox="0 0 24 10" fill="none" stroke="currentColor" stroke-width="1.6"><path d="M0 5h22M18 1l4 4-4 4"/></svg>LEARN MORE</div>
<div class="btn-more solid" style="left:520px;top:1155px"><svg width="24" height="10" viewBox="0 0 24 10" fill="none" stroke="currentColor" stroke-width="1.6"><path d="M0 5h22M18 1l4 4-4 4"/></svg>LEARN MORE</div>
<div class="btn-more" style="left:857px;top:1155px"><svg width="24" height="10" viewBox="0 0 24 10" fill="none" stroke="currentColor" stroke-width="1.6"><path d="M0 5h22M18 1l4 4-4 4"/></svg>LEARN MORE</div>
<div class="btn-more" style="left:173px;top:1611px"><svg width="24" height="10" viewBox="0 0 24 10" fill="none" stroke="currentColor" stroke-width="1.6"><path d="M0 5h22M18 1l4 4-4 4"/></svg>LEARN MORE</div>
<div class="btn-more" style="left:518px;top:1611px"><svg width="24" height="10" viewBox="0 0 24 10" fill="none" stroke="currentColor" stroke-width="1.6"><path d="M0 5h22M18 1l4 4-4 4"/></svg>LEARN MORE</div>
<div class="btn-more" style="left:857px;top:1611px"><svg width="24" height="10" viewBox="0 0 24 10" fill="none" stroke="currentColor" stroke-width="1.6"><path d="M0 5h22M18 1l4 4-4 4"/></svg>LEARN MORE</div>

<div class="btn-outline" style="left:466px;top:1697px;width:266px;height:57px;font-size:20px">VIEW ALL PRODUCTS</div>

<section class="quote"></section>
<div class="candy" style="left:1009px;top:1796px;width:191px;height:92px;background:linear-gradient(90deg,#f2b81c,#f6e6a8 40%,#f2a21c)" role="img" aria-label="Scattered yellow and orange gummy bears"></div>
<h2 class="section-title display" style="top:1895px;color:#fff">Request a Quote</h2>

<div class="field" style="left:155px;top:1988px;width:397px">FIRST NAME<svg width="13" height="14" viewBox="0 0 24 24"><circle cx="12" cy="7" r="5"/><path d="M3 23c0-6 4-9 9-9s9 3 9 9z"/></svg></div>
<div class="field" style="left:647px;top:1988px;width:397px">LAST NAME<svg width="13" height="14" viewBox="0 0 24 24"><circle cx="12" cy="7" r="5"/><path d="M3 23c0-6 4-9 9-9s9 3 9 9z"/></svg></div>
<div class="field" style="left:155px;top:2049px;width:397px">EMAIL ADDRESS<svg width="15" height="11" viewBox="0 0 24 18"><path d="M0 0h24v18H0z M2 2l10 8 10-8"/></svg></div>
<div class="field" style="left:647px;top:2049px;width:397px">PHONE NUMBER<svg width="13" height="13" viewBox="0 0 24 24"><path d="M6.6 10.8a15 15 0 0 0 6.6 6.6l2.2-2.2c.3-.3.7-.4 1-.2 1.1.4 2.3.6 3.6.6.6 0 1 .4 1 1V20c0 .6-.4 1-1 1A17 17 0 0 1 3 4c0-.6.4-1 1-1h3.5c.6 0 1 .4 1 1 0 1.3.2 2.5.6 3.6.1.3 0 .7-.2 1z"/></svg></div>
<div class="field" style="left:155px;top:2106px;width:889px;height:62px;align-items:flex-start">MESSAGE<svg width="16" height="15" viewBox="0 0 24 22"><path d="M3 0h18a3 3 0 0 1 3 3v10a3 3 0 0 1-3 3H9l-6 5v-5a3 3 0 0 1-3-3V3a3 3 0 0 1 3-3z"/></svg></div>
<div class="btn-send">SEND MESSAGE</div>

<div class="about-frame"></div>
<div class="about-photo" role="img" aria-label="Close view of red, orange and yellow gummy bears"></div>
<div class="candy" style="left:23px;top:2797px;width:206px;height:115px;border-radius:60px;background:radial-gradient(circle at 40% 50%,#e04848,#f2c23a 45%,#7ab83a 70%,rgba(255,255,255,0) 72%)" role="img" aria-label="Pile of sugared gum drops"></div>
<h2 class="abs display about-title">About Us</h2>
<p class="abs about-text">Lorem ipsum dolor sit amet, consectetur adipiscing elit, sed do eiusmod tempor incididunt ut labore et dolore magna aliqua. Ut enim ad minim veniam, quis nostrud exercitation ullamco laboris nisi ut aliquip ex ea commodo consequat.</p>
<div class="btn-outline" style="left:651px;top:2744px;width:193px;height:57px;font-size:20px">LEARN MORE</div>

<section class="careers"></section>
<div class="career-card"></div>
<div class="career-photo" role="img" aria-label="Heap of sugar-coated gummy bears in many colours"></div>
<h2 class="abs display career-title">Contact us&nbsp; for<br>Career Opportunities</h2>
<div class="field dark" style="left:168px;top:3197px;width:390px">FULL NAME<svg width="13" height="14" viewBox="0 0 24 24"><circle cx="12" cy="7" r="5"/><path d="M3 23c0-6 4-9 9-9s9 3 9 9z"/></svg></div>
<div class="field dark" style="left:168px;top:3254px;width:390px">EMAIL<svg width="15" height="11" viewBox="0 0 24 18"><path d="M0 0h24v18H0z M2 2l10 8 10-8" fill="none" stroke="#111" stroke-width="2.5"/></svg></div>
<div class="field dark" style="left:168px;top:3314px;width:390px;height:55px;align-items:flex-start">ADDRESS<svg width="11" height="15" viewBox="0 0 16 22"><path d="M8 0a8 8 0 0 1 8 8c0 6-8 14-8 14S0 14 0 8a8 8 0 0 1 8-8zm0 4a4 4 0 1 0 0 8 4 4 0 0 0 0-8z"/></svg></div>
<div class="btn-outline" style="left:168px;top:3415px;width:158px;height:49px;font-size:17px">SUBMIT NOW</div>
<div class="candy" style="left:940px;top:3493px;width:204px;height:138px;border-radius:30px;background:linear-gradient(135deg,#e8385a,#f6d23a 50%,#f08a2a)" role="img" aria-label="Stack of sugared jelly cubes"></div>

<footer class="site-footer">
  <nav class="footer-links">
    <a style="top:57px">HOME</a>
    <a style="top:103px">ABOUT US</a>
    <a style="top:149px">OUR PRODUCTS</a>
    <a style="top:195px">CONTACT US</a>
  </nav>
  <div class="footer-divider" style="left:323px"></div>
  <div class="footer-divider" style="left:821px"></div>
  <div class="footer-logo"><span class="name">HARBOR BLOOM</span><span class="sub">NUTRACEUTICAL</span></div>
  <svg class="abs" style="left:876px;top:69px" width="14" height="16" viewBox="0 0 24 26" fill="#fff"><circle cx="12" cy="7" r="5"/><path d="M3 23c0-6 4-9 9-9s9 3 9 9z"/></svg>
  <p class="footer-contact" style="top:67px">48, WHARF ROW<br>SUITE 6, BAY DISTRICT<br>052 614</p>
  <svg class="abs" style="left:876px;top:171px" width="13" height="13" viewBox="0 0 24 24" fill="#fff"><path d="M6.6 10.8a15 15 0 0 0 6.6 6.6l2.2-2.2c.3-.3.7-.4 1-.2 1.1.4 2.3.6 3.6.6.6 0 1 .4 1 1V20c0 .6-.4 1-1 1A17 17 0 0 1 3 4c0-.6.4-1 1-1h3.5c.6 0 1 .4 1 1 0 1.3.2 2.5.6 3.6.1.3 0 .7-.2 1z"/></svg>
  <p class="footer-contact" style="top:163px">+1 555 014 2290</p>
  <div class="footer-rule"></div>
  <p class="copyright">© COPYRIGHT 2024 BY HARBOR BLOOM NUTRACEUTICAL &nbsp;&nbsp;&nbsp;&nbsp;&nbsp; | &nbsp;&nbsp;&nbsp;&nbsp;&nbsp; ALL RIGHTS RESERVED</p>
</footer>

</body>
</html>
```